Velloria Flowers Florist Flyer

We are requiring a flyer that advertises and promotes our new business. We specialise in weddings and events but would also like to branch out to corporates and an online subscription. Our brand is feminine/romantic with a touch of elegance and luxury. Our main colour schemes are white, black, gold and pale pink. Instagram: Velloria_flowers and website www.velloriaflowers.com.au
Target Market(s)
brides to be, females
Industry/Entity Type
Florist
Font styles to use
Sans Serif
Script
Other font styles liked:
- The Carpenter
Colors
ffffff
000000
333333
Requirements
Must have
- Feminine/romantic feel, through use of theme colours and elegant font
- our contact details Ph: 0429518064
- email address: contactus@velloriaflowers.com.au
Nice to have
- a description of us willing to work with clients to create their dream wedding flowers. That we offer consultations and no obligation quotes.

```html
<!DOCTYPE html>
<html lang="en">
<head>
<meta charset="utf-8">
<title>Velloria Flowers – Weddings and Events Flyer</title>
<link rel="stylesheet" href="https://fonts.googleapis.com/css2?family=Inter:wght@200;300;400&display=swap">
<style>
  :root {
    --pink-light: #f9dbe9;
    --pink-mid: #f2bfd8;
    --pink-edge: #e9a9c8;
    --ornament: #e29cc0;
    --ink: #2b2b2b;
    --black: #000000;
    --white: #ffffff;
    --band: #4b4b4b;
    --leaf: #3f6b2c;
    --bloom-deep: #b81f5f;
    --bloom-rose: #f0a1b8;
    --bloom-cream: #e9e3c4;
    --bloom-peach: #e9b59a;
  }
  * { margin: 0; padding: 0; box-sizing: border-box; }
  html, body {
    width: 1002px; height: 1200px; overflow: hidden;
    background: var(--white);
  }
  .flyer {
    position: relative; width: 1002px; height: 1200px; overflow: hidden;
    background: radial-gradient(ellipse 70% 60% at 35% 35%, var(--pink-light) 0%, var(--pink-mid) 60%, var(--pink-edge) 100%);
    font-family: "Inter", "Helvetica Neue", Arial, sans-serif;
    color: var(--ink);
  }
  .bouquet {
    position: absolute;
  }
  .bouquet--left {
    left: 0; top: 0; width: 560px; height: 400px;
    background:
      radial-gradient(circle at 12% 22%, var(--bloom-deep) 0 55px, transparent 57px),
      radial-gradient(circle at 30% 38%, var(--bloom-rose) 0 48px, transparent 50px),
      radial-gradient(circle at 22% 60%, var(--bloom-deep) 0 62px, transparent 64px),
      radial-gradient(circle at 46% 55%, var(--bloom-deep) 0 50px, transparent 52px),
      radial-gradient(circle at 44% 22%, #a31433 0 42px, transparent 44px),
      radial-gradient(ellipse 62% 85% at 25% 30%, var(--leaf) 0%, rgba(63,107,44,0.6) 60%, transparent 80%);
  }
  .bouquet--right {
    right: 0; top: 0; width: 440px; height: 400px;
    background:
      radial-gradient(circle at 20% 30%, var(--bloom-cream) 0 55px, transparent 57px),
      radial-gradient(circle at 50% 20%, var(--bloom-peach) 0 50px, transparent 52px),
      radial-gradient(circle at 80% 30%, var(--bloom-cream) 0 48px, transparent 50px),
      radial-gradient(circle at 45% 60%, #d9dd9a 0 45px, transparent 47px),
      radial-gradient(circle at 70% 75%, var(--bloom-peach) 0 55px, transparent 57px),
      radial-gradient(circle at 90% 60%, var(--bloom-peach) 0 45px, transparent 47px),
      radial-gradient(ellipse 80% 85% at 60% 35%, var(--leaf) 0%, rgba(63,107,44,0.55) 65%, transparent 85%);
  }
  .bouquet--blur {
    left: 330px; top: 0; width: 300px; height: 230px;
    background: radial-gradient(ellipse 60% 70% at 50% 20%, rgba(214,120,150,0.55) 0%, transparent 75%);
    filter: blur(6px);
  }
  .ornament {
    position: absolute; left: 560px; top: 380px; width: 442px; height: 520px;
    background: radial-gradient(ellipse 55% 60% at 60% 45%, rgba(226,156,192,0.55) 0%, rgba(226,156,192,0.2) 55%, transparent 80%);
  }
  .headline {
    position: absolute; left: 80px; top: 432px; width: 440px;
    font-weight: 200; text-transform: uppercase; color: var(--ink);
    letter-spacing: -0.5px;
  }
  .headline__line { display: block; font-size: 45px; line-height: 56px; }
  .headline__line--big { font-size: 108px; line-height: 104px; letter-spacing: -2px; }
  .intro {
    position: absolute; left: 82px; top: 748px; width: 430px;
    font-size: 16.5px; line-height: 22px; font-weight: 300; color: var(--ink);
  }
  .intro p + p { margin-top: 22px; }
  .contact-band {
    position: absolute; left: 0; top: 1020px; width: 1002px; height: 180px;
    background: var(--band);
  }
  .brand-ring {
    position: absolute; left: 536px; top: 746px; width: 408px; height: 408px;
    border-radius: 50%; background: var(--pink-mid);
  }
  .brand-disc {
    position: absolute; left: 578px; top: 788px; width: 324px; height: 324px;
    border-radius: 50%; background: var(--black);
    display: flex; align-items: center; justify-content: center;
  }
  .brand-name {
    color: var(--white); font-weight: 300; font-size: 34px;
    letter-spacing: 2px; text-align: center; line-height: 1.15;
  }
  .contact-list {
    position: absolute; left: 84px; top: 1058px; list-style: none;
    color: var(--white); font-size: 18px; font-weight: 300;
  }
  .contact-list li { display: flex; align-items: center; height: 33px; }
  .contact-list svg { width: 17px; height: 17px; margin-right: 14px; fill: var(--white); }
  .social-mark {
    width: 15px; height: 15px; margin: 0 15px 0 1px; background: var(--white); border-radius: 2px;
  }
</style>
</head>
<body>
<main class="flyer">
  <div class="bouquet bouquet--blur" role="img" aria-label="Soft blurred pink flowers in the background"></div>
  <div class="bouquet bouquet--left" role="img" aria-label="Bouquet of magenta peonies, pink and red roses with green leaves"></div>
  <div class="bouquet bouquet--right" role="img" aria-label="Bouquet of cream and peach roses with white lisianthus and greenery"></div>
  <div class="ornament" role="img" aria-label="Faint pink flourish ornament"></div>

  <h1 class="headline">
    <span class="headline__line">Creating stunning</span>
    <span class="headline__line">flowers for</span>
    <span class="headline__line">weddings and</span>
    <span class="headline__line headline__line--big">Events</span>
  </h1>

  <div class="intro">
    <p>With many years of experience behind us and a combined 20 plus years in the industry. We know what we're talking about. We're here to create spectacular floral designs to suit your needs.</p>
    <p>There's nothing more frustrating than having us tell you what to do. At Velloria Flowers you are first and we're here to guide you on your floral journey.</p>
  </div>

  <div class="contact-band"></div>
  <div class="brand-ring"></div>
  <div class="brand-disc">
    <span class="brand-name">Velloria<br>Flowers</span>
  </div>

  <ul class="contact-list">
    <li>
      <svg viewBox="0 0 24 24" aria-hidden="true"><path d="M6.6 10.8a15 15 0 0 0 6.6 6.6l2.2-2.2a1 1 0 0 1 1-.25 11.4 11.4 0 0 0 3.6.57 1 1 0 0 1 1 1V20a1 1 0 0 1-1 1A17 17 0 0 1 3 4a1 1 0 0 1 1-1h3.5a1 1 0 0 1 1 1c0 1.25.2 2.45.57 3.57a1 1 0 0 1-.25 1z"/></svg>
      0429518064
    </li>
    <li>
      <svg viewBox="0 0 24 24" aria-hidden="true"><path d="M2 5h20v14H2z M3.5 6.5 12 13l8.5-6.5" fill="var(--white)" stroke="var(--band)" stroke-width="1.5"/></svg>
      contactus@velloriaflowers.com.au
    </li>
    <li>
      <span class="social-mark" aria-hidden="true"></span>
      Velloria_flowers
    </li>
  </ul>
</main>
</body>
</html>
```